Design required for boutique fire engineering firm in New Zealand

Our website was published based on free Wordpress templates, we'd like something a bit more bespoke, clean and simple.

Reason: didn't check this finished on a Sunday :)

Target Market(s)

architects, building owners, property developers

Industry/Entity Type

Boutique

Contact Information for Business Card

Logo
Fire Engineering

Derek Holloway
Principal
+64 21 738 152
derek@veltraxa.nz
veltraxa.nz

Number of Pages Required

3 page

Font styles to use
Sans Serif

Requirements
Nice to have
• On the business card, an embossed logo would be great - not sure if that's a design thing or just a print thing?
• Website, existing @ http://veltraxa.nz for extent of content and general arrangement that I'm happy with.
• Ability to update the content with project bio's and some photos at a later date would be nice.

```html
<!DOCTYPE html>
<html lang="en">
<head>
<meta charset="utf-8">
<title>Veltraxa — Fire Engineering Firm</title>
<link rel="stylesheet" href="https://fonts.googleapis.com/css2?family=Open+Sans:wght@400;600;700&family=Roboto+Condensed:wght@400;700&display=swap">
<style>
:root{
  --brand:#1f5d9e;
  --brand-dark:#174a80;
  --nav:#2f6fb1;
  --nav-active:#333a40;
  --ink:#222;
  --text:#555;
  --muted:#777;
  --light:#f2f2f2;
  --footer:#2b2b2b;
  --footer-text:#d6d6d6;
  --white:#fff;
}
*{box-sizing:border-box;margin:0;padding:0}
html,body{width:1200px;height:3103px;overflow:hidden;background:var(--white)}
body{position:relative;font-family:"Open Sans",Arial,sans-serif;color:var(--text)}
.section{position:absolute;left:0;width:1200px}
h2.section-title{font-family:"Roboto Condensed",Arial,sans-serif;font-weight:400;font-size:34px;color:var(--ink);text-align:center}

/* header */
.site-header{top:0;height:103px}
.brand{position:absolute;left:91px;top:26px;display:flex;align-items:center;gap:10px}
.brand-dot{width:50px;height:50px;border-radius:50%;background:var(--brand)}
.brand-name{font-family:"Open Sans",Arial,sans-serif;font-weight:700;font-size:40px;color:var(--brand);letter-spacing:-.5px}
.header-contact{position:absolute;right:90px;top:30px;display:flex;align-items:center;gap:14px;font-size:22px;color:#333}
.phone-icon{width:38px;height:38px;border:2px solid var(--brand);border-radius:50%;display:flex;align-items:center;justify-content:center}
.social-sq{width:20px;height:20px;background:#222;border-radius:3px}
.header-contact .social-sq:first-of-type{margin-left:14px}

/* nav */
.main-nav{top:103px;height:58px;background:var(--nav);display:flex;padding-left:89px}
.main-nav a{display:block;height:58px;line-height:58px;color:var(--white);text-decoration:none;font-size:17px;padding:0 28px}
.main-nav a.active{background:var(--nav-active);padding:0 34px}
.main-nav a.wide{padding:0 36px}

/* hero */
.hero{top:161px;height:560px}
.hero-photo{position:absolute;inset:0;background:linear-gradient(180deg,#8c98a4 0%,#6e7c86 35%,#5b6a64 65%,#7a7a3c 100%)}
.hero-text{position:absolute;top:160px;width:100%;text-align:center;color:var(--white)}
.hero-text h1{font-family:"Open Sans",Arial,sans-serif;font-weight:400;font-size:72px;letter-spacing:1px;line-height:1}
.hero-text p{font-size:36px;margin-top:14px}
.hero-arrows{position:absolute;right:108px;top:400px;color:var(--white);font-size:24px;letter-spacing:12px}
.hero-curve{position:absolute;left:0;bottom:0}

/* welcome */
.welcome{top:790px;height:480px}
.welcome .lead{width:844px;margin:30px auto 0;text-align:center;font-size:14px;line-height:2.1;color:var(--muted)}
.services{display:flex;justify-content:center;gap:80px;margin-top:58px}
.service{width:240px;text-align:center}
.service-icon{width:104px;height:104px;margin:0 auto}
.service h3{font-weight:400;font-size:22px;color:var(--ink);margin-top:20px}
.service p{font-size:13px;line-height:1.85;color:var(--muted);margin-top:10px}
.service a{display:inline-block;font-size:13px;color:var(--brand);text-decoration:none;margin-top:4px}

/* what we do */
.what-we-do{top:1289px;height:484px;background:linear-gradient(120deg,#2c5f9c,#3a74b4 50%,#2a5a94)}
.wwd-card{position:absolute;left:149px;top:89px;width:896px;height:325px;background:var(--white);display:flex;box-shadow:0 4px 14px rgba(0,0,0,.25)}
.wwd-copy{width:507px;padding:42px 40px}
.wwd-copy h2{font-family:"Roboto Condensed",Arial,sans-serif;font-weight:400;font-size:34px;color:var(--ink)}
.wwd-copy p{font-size:14px;line-height:1.85;color:var(--text);margin-top:18px}
.btn{display:inline-block;background:var(--brand-dark);color:var(--white);font-size:13px;padding:9px 20px;border-radius:20px;text-decoration:none;margin-top:24px}
.wwd-photo{flex:1;background:linear-gradient(135deg,#9a6a48,#5d6f88 50%,#c9b9a2)}

/* projects */
.projects{top:1850px;height:440px}
.project-grid{display:flex;justify-content:center;gap:36px;margin-top:36px}
.project{width:318px}
.project-photo{height:193px;border:4px solid #e8e8e8}
.project h3{font-weight:400;font-size:17px;color:var(--ink);margin-top:24px}
.project p{font-size:13.5px;line-height:1.8;color:var(--text);margin-top:6px}
.project a{font-size:12px;color:var(--brand);text-decoration:none}
.ph-team{background:linear-gradient(135deg,#d9c7a6,#c4755a 55%,#e6ddd0)}
.ph-building{background:linear-gradient(160deg,#6d9ed4,#3f5f80 55%,#9bb27a)}
.ph-site{background:linear-gradient(140deg,#b38a63,#6f5b4a 55%,#c7b39a)}

/* blog */
.blog{top:2321px;height:480px;background:var(--light)}
.blog .section-title{margin-top:64px}
.blog-grid{display:flex;justify-content:center;gap:29px;margin-top:36px}
.post{width:499px;height:188px;background:var(--white);display:flex;box-shadow:0 2px 6px rgba(0,0,0,.12)}
.post-photo{width:165px}
.ph-firefighter{background:linear-gradient(160deg,#d9a62a,#3c3c3c 60%,#a88a46)}
.ph-workers{background:linear-gradient(160deg,#3a2f28,#b07a2a 50%,#2b2622)}
.post-body{padding:26px 22px 0 24px}
.post h3{font-weight:400;font-size:16px;color:var(--ink)}
.post time{display:block;font-size:13px;color:var(--muted);margin-top:4px}
.post p{font-size:13.5px;line-height:1.55;color:var(--text);margin-top:6px;text-align:justify}
.post a{display:block;font-size:13.5px;color:var(--brand);text-decoration:none;margin-top:8px}

/* footer */
.site-footer{top:2740px;height:363px}
.footer-curve{position:absolute;left:0;top:0}
.footer-inner{position:absolute;left:0;top:50px;width:1200px;height:313px;background:var(--footer)}
.footer-brand{position:absolute;left:99px;top:116px;display:flex;align-items:center;gap:10px}
.footer-brand .brand-dot{width:44px;height:44px;background:var(--white)}
.footer-brand .brand-name{color:var(--white);font-size:36px}
.footer-col{position:absolute;top:72px;color:var(--footer-text);font-size:11.5px}
.footer-col h4{font-weight:400;font-size:13px;color:var(--white);margin-bottom:22px}
.footer-col address{font-style:normal;line-height:2.05}
.col-contact{left:414px}
.col-mail{left:662px;width:230px}
.col-mail p{line-height:1.6}
.signup{display:flex;margin-top:16px}
.signup span{width:142px;height:28px;background:var(--white);color:#999;font-size:11px;line-height:28px;padding-left:8px}
.signup b{width:60px;height:28px;background:var(--nav);color:var(--white);font-weight:400;font-size:12px;line-height:28px;text-align:center}
.col-social{left:950px}
.social-row{display:flex;gap:14px}
.social-row .social-sq{width:24px;height:24px;background:var(--white)}
.footer-rule{position:absolute;left:91px;right:91px;top:228px;border-top:1px solid #444}
.copyright{position:absolute;top:260px;width:100%;text-align:center;color:var(--white);font-size:12px}
</style>
</head>
<body>

<header class="section site-header">
  <div class="brand"><span class="brand-dot"></span><span class="brand-name">veltraxa</span></div>
  <div class="header-contact">
    <span class="phone-icon"><svg width="18" height="18" viewBox="0 0 24 24"><path d="M6.6 10.8a15 15 0 0 0 6.6 6.6l2.2-2.2a1 1 0 0 1 1-.25 11.4 11.4 0 0 0 3.6.57 1 1 0 0 1 1 1V20a1 1 0 0 1-1 1A17 17 0 0 1 3 4a1 1 0 0 1 1-1h3.5a1 1 0 0 1 1 1c0 1.25.2 2.45.57 3.6a1 1 0 0 1-.25 1z" fill="#1f5d9e"/></svg></span>
    <span>021 738 152</span>
    <span class="social-sq"></span><span class="social-sq"></span>
  </div>
</header>

<nav class="section main-nav">
  <a class="active" href="#">Home</a>
  <a class="wide" href="#">About us</a>
  <a class="wide" href="#">Services</a>
  <a class="wide" href="#">Projects</a>
  <a class="wide" href="#">Blog</a>
  <a class="wide" href="#">Support</a>
  <a class="wide" href="#">Contact Us</a>
</nav>

<section class="section hero">
  <div class="hero-photo" role="img" aria-label="City skyline with harbour and a hillside in the foreground"></div>
  <div class="hero-text">
    <h1>VELTRAXA</h1>
    <p>Fire Engineering Firm</p>
  </div>
  <div class="hero-arrows">&lsaquo;&rsaquo;</div>
  <svg class="hero-curve" width="1200" height="90" viewBox="0 0 1200 90" aria-hidden="true">
    <path d="M0 10 Q600 110 1200 0 L1200 90 L0 90 Z" fill="#1f5d9e"/>
    <path d="M0 22 Q600 118 1200 14 L1200 90 L0 90 Z" fill="#fff"/>
  </svg>
</section>

<section class="section welcome">
  <h2 class="section-title">Welcome To Veltraxa</h2>
  <p class="lead">Veltraxa is a boutique fire engineering firm based in Wellington, New Zealand, founded by Derek Holloway in 2017. We provide consulting services in the built environment, including design and review services to assist in Building Consent applications, advice on property protection matters, observation of construction on site, and regulatory consultation</p>
  <div class="services">
    <div class="service">
      <svg class="service-icon" viewBox="0 0 104 104" aria-hidden="true">
        <circle cx="52" cy="52" r="46" fill="none" stroke="#1f5d9e" stroke-width="6" stroke-dasharray="64 8"/>
        <circle cx="52" cy="52" r="34" fill="#1f5d9e"/>
        <path d="M52 30c4 8 12 12 12 22a12 12 0 0 1-24 0c0-6 4-9 5-13 2 4 3 6 5 7 0-6 0-11 2-16z" fill="#fff"/>
      </svg>
      <h3>Fire Engineering</h3>
      <p>It is a long established fact that a reader will be distracted by the readable</p>
      <a href="#">Learn More -&gt;</a>
    </div>
    <div class="service">
      <svg class="service-icon" viewBox="0 0 104 104" aria-hidden="true">
        <circle cx="52" cy="52" r="46" fill="none" stroke="#1f5d9e" stroke-width="6" stroke-dasharray="64 8"/>
        <circle cx="52" cy="52" r="34" fill="#1f5d9e"/>
        <rect x="44" y="38" width="16" height="30" rx="3" fill="#fff"/>
        <rect x="38" y="48" width="28" height="7" rx="2" fill="#fff"/>
        <rect x="40" y="67" width="24" height="5" fill="#fff"/>
        <circle cx="52" cy="36" r="5" fill="#fff"/>
      </svg>
      <h3>Fire Protection</h3>
      <p>It is a long established fact that a reader will be distracted by the readable</p>
      <a href="#">Learn More -&gt;</a>
    </div>
    <div class="service">
      <svg class="service-icon" viewBox="0 0 104 104" aria-hidden="true">
        <circle cx="52" cy="52" r="46" fill="none" stroke="#1f5d9e" stroke-width="6" stroke-dasharray="64 8"/>
        <circle cx="52" cy="52" r="34" fill="#1f5d9e"/>
        <circle cx="40" cy="44" r="5" fill="#fff"/><circle cx="64" cy="44" r="5" fill="#fff"/><circle cx="52" cy="41" r="6" fill="#fff"/>
        <path d="M32 64a8 8 0 0 1 16 0zM56 64a8 8 0 0 1 16 0zM42 66a10 10 0 0 1 20 0z" fill="#fff"/>
      </svg>
      <h3>Advisory Consulting</h3>
      <p>It is a long established fact that a reader will be distracted by the readable content</p>
      <a href="#">Learn More -&gt;</a>
    </div>
  </div>
</section>

<section class="section what-we-do">
  <div class="wwd-card">
    <div class="wwd-copy">
      <h2>What We Do</h2>
      <p>Veltraxa is a boutique fire engineering firm based in Wellington, New Zealand, founded by Derek Holloway in 2017. We provide consulting services in the built environment, including design and review services to assist in Building Consent applications, advice on property protection matters, observation of construction on site, and regulatory consultation</p>
      <a class="btn" href="#">Read More</a>
    </div>
    <div class="wwd-photo" role="img" aria-label="Technician in a hard hat inspecting sprinkler pipework"></div>
  </div>
</section>

<section class="section projects">
  <h2 class="section-title">Latest Projects</h2>
  <div class="project-grid">
    <article class="project">
      <div class="project-photo ph-team" role="img" aria-label="Construction team in hard hats on site"></div>
      <h3>Porro quisquam est</h3>
      <p>It has survived not only five centuries, but also the leap into electronic typesetting,</p>
      <a href="#">Read More &raquo;</a>
    </article>
    <article class="project">
      <div class="project-photo ph-building" role="img" aria-label="Modern glass office building beside trees"></div>
      <h3>Dolorem ipsum quia</h3>
      <p>It has survived not only five centuries, but also the leap into electronic typesetting, remaining</p>
      <a href="#">Read More &raquo;</a>
    </article>
    <article class="project">
      <div class="project-photo ph-site" role="img" aria-label="Engineers reviewing a building under construction"></div>
      <h3>Neque porro quisquam</h3>
      <p>It has survived not only five centuries, but also the leap into electronic typesetting, remaining</p>
      <a href="#">Read More &raquo;</a>
    </article>
  </div>
</section>

<section class="section blog">
  <h2 class="section-title">Latest Blog</h2>
  <div class="blog-grid">
    <article class="post">
      <div class="post-photo ph-firefighter" role="img" aria-label="Firefighter in full protective gear"></div>
      <div class="post-body">
        <h3>Nemo Enim Ipsam Volup</h3>
        <time>09-07-2017</time>
        <p>Lorem Ipsum has been the industry's standard dummy text ever since the 1500s, when an unknown printer took a galley</p>
        <a href="#">Read More &gt;&gt;</a>
      </div>
    </article>
    <article class="post">
      <div class="post-photo ph-workers" role="img" aria-label="Workers in hard hats inspecting a site at night"></div>
      <div class="post-body">
        <h3>Nemo Enim Ipsam Volup</h3>
        <time>09-07-2017</time>
        <p>Lorem Ipsum has been the industry's standard dummy text ever since the 1500s, when an unknown printer took a galley</p>
        <a href="#">Read More &gt;&gt;</a>
      </div>
    </article>
  </div>
</section>

<footer class="section site-footer">
  <svg class="footer-curve" width="1200" height="64" viewBox="0 0 1200 64" aria-hidden="true">
    <path d="M0 60 Q600 -40 1200 60 Z" fill="#2f6fb1"/>
    <path d="M0 64 Q600 -24 1200 64 Z" fill="#2b2b2b"/>
  </svg>
  <div class="footer-inner">
    <div class="footer-brand"><span class="brand-dot"></span><span class="brand-name">veltraxa</span></div>
    <div class="footer-col col-contact">
      <h4>CONTACT US</h4>
      <address>Address : P.O. Box 3186<br>Tarrin, NC 27604<br>Phone : 021 738 152<br>Email : info@veltraxa.nz</address>
    </div>
    <div class="footer-col col-mail">
      <h4>JOIN OUR MAILING LIST</h4>
      <p>Your about us information would fit here nicely.</p>
      <div class="signup"><span>Email address</span><b>Submit</b></div>
    </div>
    <div class="footer-col col-social">
      <h4>FOLLOW US OUT THERE</h4>
      <div class="social-row"><span class="social-sq"></span><span class="social-sq"></span><span class="social-sq"></span><span class="social-sq"></span></div>
    </div>
    <div class="footer-rule"></div>
    <p class="copyright">Copyright © 2017 All Rights Reserved</p>
  </div>
</footer>

</body>
</html>
```